Business Card Design Coralgate Airflow Solutions

The Business will be centred around supply and installation of Ventilation for domestic homes and warehousing/workshops, and will be marketed as a Eco friendly means of reducing your carbon footprint and reducing energy consumption.Our suppliers will provide a range of products that will ventilate roof spaces and later will branch into to air transfer within homes for cooling and heating other rooms of the home etc.I would like to see colours that would be commensurate with the logo provided and yet not dominate the logo.Final design should convey a Diverse , professional but friendly service that will suit client needs

Target Market(s)

Domestic home owners and warehousing/workshop businesses

Industry/Entity Type

Business

Contact Information for Business Card

Company Name: Coralgate Airflow Solutions Pty Ltd, ABN: 42 817 359 264, Address: 27 Marrowfen Tulvanna W.A 6289, Email: dale@coralgateairflowsolutions.com.au, Mobile Number: 0461 852 309

Requirements
Nice to have
• A tract art that commensurate of the logo supplied
Should not have
• Font style that opposes logo design

```html
<!DOCTYPE html>
<html lang="en">
<head>
<meta charset="utf-8">
<title>Coralgate Airflow Solutions – Business Card</title>
<link rel="stylesheet" href="https://fonts.googleapis.com/css2?family=Open+Sans:wght@400;600;700&display=swap">
<style>
  :root {
    --backdrop: #3a332e;
    --card: #1b1b1c;
    --card-edge: #2a2a2b;
    --green: #22b04b;
    --white: #f2f2f2;
    --divider: #3c3c3e;
  }
  * { box-sizing: border-box; margin: 0; padding: 0; }
  html, body {
    width: 1200px; height: 844px; overflow: hidden;
    background: var(--backdrop);
    font-family: "Open Sans", Arial, sans-serif;
  }
  .stage {
    position: relative; width: 1200px; height: 844px;
    display: flex; align-items: center; justify-content: center; gap: 60px;
  }
  .card {
    position: relative; width: 510px; height: 292px; overflow: hidden;
    background: var(--card);
    border: 1px solid var(--card-edge);
    box-shadow: 0 10px 30px rgba(0,0,0,.45);
  }
  .brand {
    display: flex; align-items: center; gap: 10px;
    color: var(--white); font-weight: 600; white-space: nowrap;
  }
  .brand-mark { width: 14px; height: 14px; background: var(--green); flex: none; }

  /* contact side */
  .card-contact .brand {
    position: absolute; top: 62px; left: 0; right: 0; justify-content: center;
    font-size: 24px;
  }
  .person {
    position: absolute; top: 150px; left: 14px; width: 170px; text-align: right;
  }
  .person-name { color: var(--green); font-weight: 700; font-size: 20px; line-height: 1.2; white-space: nowrap; }
  .person-role { color: var(--white); font-size: 14px; margin-top: 2px; white-space: nowrap; }
  .person-address { color: var(--white); font-size: 14px; line-height: 1.35; margin-top: 16px; white-space: nowrap; }
  .divider {
    position: absolute; top: 150px; left: 200px; width: 1px; height: 104px;
    background: var(--divider);
  }
  .contact-list {
    position: absolute; top: 146px; left: 214px; right: 14px; list-style: none;
  }
  .contact-list li {
    display: flex; align-items: center; gap: 9px;
    color: var(--white); font-size: 12.5px; height: 26px; white-space: nowrap;
  }
  .icon {
    width: 17px; height: 17px; background: var(--green); border-radius: 2px;
    display: flex; align-items: center; justify-content: center; flex: none;
  }
  .icon svg { width: 11px; height: 11px; fill: none; stroke: #fff; stroke-width: 1.6; stroke-linecap: round; stroke-linejoin: round; }

  /* logo side */
  .card-front .brand {
    position: absolute; inset: 0; justify-content: center; font-size: 28px;
  }
</style>
</head>
<body>
<main class="stage">
  <section class="card card-contact" aria-label="Business card, contact side">
    <div class="brand"><span class="brand-mark"></span>Coralgate Airflow Solutions</div>

    <div class="person">
      <p class="person-name">Dale Harrow</p>
      <p class="person-role">Managing Director</p>
      <p class="person-address">27 Marrowfen Tulvanna<br>W.A 6289</p>
    </div>

    <div class="divider"></div>

    <ul class="contact-list">
      <li>
        <span class="icon"><svg viewBox="0 0 12 12"><path d="M2.5 1.5l2 .5.6 2-1.2 1a6 6 0 0 0 3 3l1-1.2 2 .6.5 2c-4.5.5-8.5-3.5-8-7.9z"/></svg></span>
        0461 852 309
      </li>
      <li>
        <span class="icon"><svg viewBox="0 0 12 12"><rect x="3" y="1" width="6" height="10" rx="1"/><path d="M5.3 9.2h1.4"/></svg></span>
        08 9524 6170
      </li>
      <li>
        <span class="icon"><svg viewBox="0 0 12 12"><rect x="1.2" y="2.5" width="9.6" height="7" rx=".6"/><path d="M1.5 3l4.5 3.5L10.5 3"/></svg></span>
        dale@coralgateairflowsolutions.com.au
      </li>
      <li>
        <span class="icon"><svg viewBox="0 0 12 12"><path d="M5 7l2-2M4.2 5.8L3 7a1.5 1.5 0 0 0 2 2l1.2-1.2M7.8 6.2L9 5a1.5 1.5 0 0 0-2-2L5.8 4.2"/></svg></span>
        www.coralgateairflowsolutions.com.au
      </li>
    </ul>
  </section>

  <section class="card card-front" aria-label="Business card, logo side">
    <div class="brand"><span class="brand-mark"></span>Coralgate Airflow Solutions</div>
  </section>
</main>
</body>
</html>
```